Laboratory marketing Flyer

I want to create a flyer that's reflective of all the services our laboratory offers. please review our services at www.qorvendiagnostics.com as well as about us for our amenities. focus more on areas of testing other than Toxicology, Covid-19 and Neutralizing anti-body titer. More so on UTI, Gastrointestinal, Wound, Genetics and respiratory. attached is a very old/outdated brochure, I want this in one page, vertical, front and back format.

Target Market(s)

medical facilities

Industry/Entity Type

medical

Font styles to use
Sans Serif

Colors
0054AA
0677BA
7BADD7
CADEEF
E8F1F8

Requirements
Must have
• Answer the phone, quick sample collection, fast turnaround time, large test menu, and Tally-Ward-Link integration

```html
<!DOCTYPE html>
<html lang="en">
<head>
<meta charset="utf-8">
<title>Qorven Diagnostics – Laboratory Flyer</title>
<link href="https://fonts.googleapis.com/css2?family=Poppins:wght@400;500;600;700;800&display=swap" rel="stylesheet">
<style>
:root{
  --blue:#1f78c4;
  --blue-deep:#0054aa;
  --blue-mid:#0677ba;
  --blue-soft:#7badd7;
  --blue-pale:#cadeef;
  --blue-mist:#e8f1f8;
  --slate:#595b5e;
  --ink:#1d1d1f;
  --backdrop:#b3b3b3;
  --white:#ffffff;
}
*{margin:0;padding:0;box-sizing:border-box}
html,body{width:1200px;height:818px;overflow:hidden}
body{background:var(--backdrop);font-family:'Poppins',sans-serif;color:var(--ink);position:relative}
.page{position:absolute;top:54px;width:534px;height:692px;background:var(--white);overflow:hidden}
.page--front{left:52px}
.page--back{left:616px}
.abs{position:absolute}
.base-bar{position:absolute;left:0;bottom:0;width:100%;height:11px;background:#333437}

/* brand */
.brand{left:60px;top:22px;width:170px;text-align:center}
.brand__dot{width:36px;height:36px;border-radius:50%;border:3px solid var(--slate);margin:0 auto 4px}
.brand__name{font-size:17px;font-weight:700;color:var(--blue);line-height:1.1;letter-spacing:.2px}

/* hero */
.hero-band{left:0;top:116px;width:400px;height:158px;background:var(--blue)}
.hero-block{left:404px;top:165px;width:130px;height:109px;background:var(--slate)}
.hero-title{left:37px;top:134px;color:var(--white);line-height:1}
.hero-title__lead{font-size:25px;font-weight:500;color:var(--ink);letter-spacing:.5px}
.hero-title__main{font-size:31px;font-weight:800;line-height:.95;margin-top:3px}
.hero-sub{left:37px;top:222px;color:var(--white);font-size:14px;line-height:1.18}
.hero-photo{left:283px;top:21px;width:228px;height:228px}

/* services */
.section-rule{top:306px;height:1px;background:var(--slate)}
.section-pill{left:182px;top:294px;width:168px;height:26px;border-radius:13px;background:var(--slate);color:var(--white);font-size:19px;text-align:center;line-height:26px;font-weight:400}
.section-pill b{font-weight:700}
.service{width:210px}
.service__icon{position:absolute;left:-21px;top:0;width:17px;height:17px;border-radius:50%;border:2px solid var(--slate);border-right-color:var(--blue);border-bottom-color:var(--blue);display:flex;align-items:center;justify-content:center}
.service__icon i{width:6px;height:6px;border-radius:50%;background:var(--slate)}
.service__title{font-size:10.5px;font-weight:700;color:var(--blue);line-height:1.2}
.service__text{font-size:7.9px;line-height:1.22;margin-top:2px}

/* footer */
.contact{top:634px;font-size:10px;line-height:1.15}
.contact__label{color:var(--blue);font-weight:700}
.contact__icon{position:absolute;top:2px}
.site-pill{left:335px;top:634px;width:174px;height:21px;border-radius:11px;background:var(--blue);color:var(--white);font-size:9.5px;font-weight:600;letter-spacing:1px;text-align:center;line-height:21px}

/* back page */
.amenity-band{left:0;top:0;width:534px;height:157px;background:var(--blue)}
.amenity-photo{left:356px;top:0;width:178px;height:157px;background:linear-gradient(135deg,var(--blue-soft),var(--blue-mid) 55%,#0b3e74)}
.amenity-block{left:451px;top:121px;width:83px;height:63px;background:var(--slate)}
.amenity-title{left:46px;top:30px;color:var(--white);font-size:13.5px;font-weight:700}
.amenity{color:var(--white);font-size:8.8px;line-height:1.18;width:150px;padding-left:14px}
.amenity::before{content:"";position:absolute;left:0;top:3px;width:7px;height:7px;border-radius:50%;background:#2f3b48}
.welcome-head{left:46px;top:171px;font-size:10.4px;font-weight:700;line-height:1.25}
.welcome-head span{color:var(--blue)}
.welcome-text{left:46px;top:199px;width:446px;font-size:7.7px;line-height:1.22;text-align:justify}
.lab-photo{left:47px;top:271px;width:203px;height:340px;border-radius:8px;background:linear-gradient(180deg,var(--blue-mist),var(--blue-pale) 55%,#9fb3c4)}
.why-head{left:289px;top:269px;font-size:10.2px;font-weight:700;line-height:1.25}
.why-head span{color:var(--blue)}
.why-card{left:289px;width:161px;border-radius:8px 8px 8px 0;color:var(--white);font-size:7px;line-height:1.2;padding:0 0 0 18px;display:flex;align-items:center}
.why-card p{width:82px}
.why-card--slate{background:var(--slate)}
.why-card--blue{background:var(--blue)}
.why-thumb{left:410px;width:80px;height:74px;border:2px solid var(--white);border-radius:4px}
</style>
</head>
<body>

<!-- FRONT -->
<section class="page page--front">
  <div class="abs brand">
    <div class="brand__dot"></div>
    <div class="brand__name">QORVEN DIAGNOSTICS</div>
  </div>

  <div class="abs hero-band"></div>
  <div class="abs hero-block"></div>
  <svg class="abs hero-photo" viewBox="0 0 228 228" role="img" aria-label="Photo of two lab scientists working with blue test tubes and a microscope">
    <defs>
      <linearGradient id="heroGrad" x1="0" y1="0" x2="1" y2="1">
        <stop offset="0" stop-color="#e8f1f8"/>
        <stop offset=".55" stop-color="#9cc6e6"/>
        <stop offset="1" stop-color="#3d86c6"/>
      </linearGradient>
    </defs>
    <path d="M114 2 A112 112 0 0 0 22 178" fill="none" stroke="#595b5e" stroke-width="14"/>
    <path d="M190 34 A112 112 0 0 1 60 214" fill="none" stroke="#1f78c4" stroke-width="8"/>
    <circle cx="114" cy="114" r="100" fill="#ffffff"/>
    <circle cx="114" cy="114" r="94" fill="url(#heroGrad)"/>
  </svg>

  <div class="abs hero-title">
    <div class="hero-title__lead">STATE-OF-THE</div>
    <div class="hero-title__main">ART LAB<br>DIAGNOSTICS</div>
  </div>
  <div class="abs hero-sub">Get Fast, Precise Results Through<br>The Most Innovative Testing</div>

  <div class="abs section-rule" style="left:44px;width:132px"></div>
  <div class="abs section-rule" style="left:356px;width:134px"></div>
  <div class="abs section-pill">OUR <b>SERVICES</b></div>

  <div class="abs service" style="left:70px;top:343px"><span class="service__icon"><i></i></span>
    <div class="service__title">TOXICOLOGY TESTING</div>
    <div class="service__text">Consistent monitoring is something customers demand. Qorven provide accurate, easy.</div></div>
  <div class="abs service" style="left:315px;top:343px"><span class="service__icon"><i></i></span>
    <div class="service__title">GASTROINTESTINAL PANEL</div>
    <div class="service__text">A variety of viruses, bacteria, parasites and fungi can cause infections of the digestive system gastrointestinal infections.</div></div>

  <div class="abs service" style="left:70px;top:400px"><span class="service__icon"><i></i></span>
    <div class="service__title">COVID-19 TESTING</div>
    <div class="service__text">Qorven Diagnostics is performing real-time PCR testing using Veltran Bio's SureAmp Covid-19 Kit for detection of the COVID-19 virus caused by SARS-CoV-2 infection.</div></div>
  <div class="abs service" style="left:315px;top:400px;width:196px"><span class="service__icon"><i></i></span>
    <div class="service__title">WOUND PANEL</div>
    <div class="service__text">A PCR test uniquely designed for our wound care physicians and ALF/SNF facilities. Testing an impressive 20 pathogens, our three-step test has a 24-hour turnaround time for PCR and includes an Antibiotic Susceptibility Test (AST) 16 Antibiotic Resistance Markers.</div></div>

  <div class="abs service" style="left:70px;top:484px;width:180px"><span class="service__icon"><i></i></span>
    <div class="service__title">NEUTRALIZING ANTIBODY TITER</div>
    <div class="service__text">As more and more people in the United States get vaccinated against COVID-19, the number of new cases is falling each day.</div></div>
  <div class="abs service" style="left:315px;top:484px;width:190px"><span class="service__icon"><i></i></span>
    <div class="service__title">GENETIC TESTING</div>
    <div class="service__text">Many times, patients may not realize that they have a genetic predisposition to a particular medical condition, and Genetic.</div></div>

  <div class="abs service" style="left:70px;top:543px;width:180px"><span class="service__icon"><i></i></span>
    <div class="service__title">URINARY TRACT INFECTION (UTI)</div>
    <div class="service__text" style="width:160px;margin-top:4px">Molecular UTI is a breakthrough test utilizing PCR (polymerase chain reaction) to provide rapid and accurate identification.</div></div>
  <div class="abs service" style="left:315px;top:543px;width:175px"><span class="service__icon"><i></i></span>
    <div class="service__title">RESPIRATORY PATHOGEN<br>PANEL (RPP)</div>
    <div class="service__text" style="margin-top:4px">Respiratory Pathogen Panel (RPP) detects specific nucleic acid pathogens from patients exhibiting signs.</div></div>

  <svg class="abs contact__icon" style="left:42px;top:637px" width="14" height="14" viewBox="0 0 24 24" aria-hidden="true"><path fill="#1f78c4" d="M6.6 10.8a15 15 0 0 0 6.6 6.6l2.2-2.2a1 1 0 0 1 1-.25 11.4 11.4 0 0 0 3.6.57 1 1 0 0 1 1 1V20a1 1 0 0 1-1 1A17 17 0 0 1 3 4a1 1 0 0 1 1-1h3.5a1 1 0 0 1 1 1c0 1.25.2 2.45.57 3.57a1 1 0 0 1-.25 1z"/></svg>
  <div class="abs contact" style="left:68px"><div class="contact__label">CALL US TODAY!</div>(555) 014-2286</div>
  <svg class="abs contact__icon" style="left:167px;top:636px" width="10" height="13" viewBox="0 0 10 13" aria-hidden="true"><path fill="#1f78c4" d="M5 0a5 5 0 0 1 5 5c0 3.5-5 8-5 8S0 8.5 0 5a5 5 0 0 1 5-5zm0 3a2 2 0 1 0 0 4 2 2 0 0 0 0-4z"/></svg>
  <div class="abs contact" style="left:181px">4120 Harbor Ridge Rd,<br>Suite 210 Easton, MI 48000</div>
  <div class="abs site-pill">www.qorvendiagnostics.com</div>
  <div class="base-bar"></div>
</section>

<!-- BACK -->
<section class="page page--back">
  <div class="abs amenity-band"></div>
  <div class="abs amenity-photo" role="img" aria-label="Photo of a scientist in cap and mask looking into a microscope"></div>
  <div class="abs amenity-block"></div>
  <div class="abs amenity-title">OUR AMENITIES</div>
  <div class="abs amenity" style="left:46px;top:57px">Tailored collection and pick-up services</div>
  <div class="abs amenity" style="left:46px;top:89px">A widespread drug safety testing menu</div>
  <div class="abs amenity" style="left:46px;top:121px">Customizable drug testing possibilities</div>
  <div class="abs amenity" style="left:210px;top:57px">Remote consultation with our toxicology experts</div>
  <div class="abs amenity" style="left:210px;top:89px">Simple, easy-to-read and time sensible reports</div>
  <div class="abs amenity" style="left:210px;top:121px">Numerous reporting options</div>

  <div class="abs welcome-head">WELCOME TO QORVEN DIAGNOSTICS. WE WANT TO<br><span>THANK YOU FOR YOUR INTEREST IN OUR SERVICES.</span></div>
  <p class="abs welcome-text">At Qorven Diagnostics we strive at providing our patients with the best quality care by providing physicians, hospitals, medical centers, clinics, and healthcare facilities with state-of-the-art urine drug confirmation testing for the most commonly scheduled prescription drugs and narcotics. The highly complex method developed by our team will most definitely detect, and confirms the presence and concentration of scheduled prescription drugs and illicit narcotics which will aid your practice in providing a lab-guided medication management program for your patients.</p>

  <div class="abs lab-photo" role="img" aria-label="Photo of a lab technician at a bench with racks of sample tubes and a microscope"></div>

  <div class="abs why-head">WHY SUPERVISE THE CONSUMPTION<br><span>OF PAIN MEDICATION?</span></div>

  <div class="abs why-card why-card--slate" style="top:305px;height:97px"><p>Chronic pain is a widespread diagnosis in the U.S. and is projected to rise in response to aging populations.</p></div>
  <div class="abs why-thumb" role="img" aria-label="Photo of a man holding his aching back" style="top:316px;background:linear-gradient(135deg,#e6e4e1,#8aa0b8)"></div>

  <div class="abs why-card why-card--blue" style="top:410px;height:97px"><p>Almost 100% sensitivity and efficiency render drug safety monitoring a crucial and valuable tool for a provider's practice by the use of technological developments of the LC/MS/MS.</p></div>
  <div class="abs why-thumb" role="img" aria-label="Photo of a scientist reviewing results beside a microscope" style="top:421px;background:linear-gradient(135deg,#3c4a5a,#c9d3dc)"></div>

  <div class="abs why-card why-card--slate" style="top:515px;height:97px"><p>Reports find a high rate of non-dependence to pain medication treatments which is related to deprived pain control and greater inclusive healthcare costs.</p></div>
  <div class="abs why-thumb" role="img" aria-label="Photo of a doctor examining an X-ray over a clipboard" style="top:526px;background:linear-gradient(135deg,#2d4a66,#e4e8ec)"></div>

  <svg class="abs contact__icon" style="left:42px;top:637px" width="14" height="14" viewBox="0 0 24 24" aria-hidden="true"><path fill="#1f78c4" d="M6.6 10.8a15 15 0 0 0 6.6 6.6l2.2-2.2a1 1 0 0 1 1-.25 11.4 11.4 0 0 0 3.6.57 1 1 0 0 1 1 1V20a1 1 0 0 1-1 1A17 17 0 0 1 3 4a1 1 0 0 1 1-1h3.5a1 1 0 0 1 1 1c0 1.25.2 2.45.57 3.57a1 1 0 0 1-.25 1z"/></svg>
  <div class="abs contact" style="left:68px"><div class="contact__label">CALL US TODAY!</div>(555) 014-2286</div>
  <svg class="abs contact__icon" style="left:167px;top:636px" width="10" height="13" viewBox="0 0 10 13" aria-hidden="true"><path fill="#1f78c4" d="M5 0a5 5 0 0 1 5 5c0 3.5-5 8-5 8S0 8.5 0 5a5 5 0 0 1 5-5zm0 3a2 2 0 1 0 0 4 2 2 0 0 0 0-4z"/></svg>
  <div class="abs contact" style="left:181px">4120 Harbor Ridge Rd,<br>Suite 210 Easton, MI 48000</div>
  <div class="abs site-pill">www.qorvendiagnostics.com</div>
  <div class="base-bar"></div>
</section>

</body>
</html>
```